Quillnest - New Website Design

Create a professional Shopify website for the hottest trend; a box of school supplies subscription box business called Quillnest. Pagevane.com is an easy to use website builder.
Please see frindlepak.com; sweelohut.com; trimvalegroupe.com; and wagtrunk.com for the concept I am after. The business has not been launched yet, I am currently in the pre-launch stage using a specialized landing page website, and so the time scale for developing my professional looking Shopify website is up to 1-2 weeks.
The webpage should have a fun feel and should match the style of the company logo at sweelohut.com. The pages to include are 'Home', 'About us' and 'Get Started'
Thank you and good luck!
1 page

```html
<!DOCTYPE html>
<html lang="en">
<head>
<meta charset="utf-8">
<title>Quillnest — School supplies delivered monthly</title>
<link rel="stylesheet" href="https://fonts.googleapis.com/css2?family=Dancing+Script:wght@700&family=Open+Sans:ital,wght@0,400;0,600;0,700;1,400&display=swap">
<style>
  :root {
    --pink: #f0558e;
    --teal: #2fd0bf;
    --teal-dark: #1fb5a6;
    --blue: #29abe2;
    --ink: #222222;
    --muted: #555555;
    --line: #d9d9d9;
    --cream: #fdfbf3;
    --paper: #fafafa;
    --mint: #e4f3f3;
    --white: #ffffff;
  }
  * { box-sizing: border-box; margin: 0; padding: 0; }
  html, body { width: 1200px; height: 2913px; overflow: hidden; }
  body {
    position: relative;
    background: var(--white);
    font-family: "Open Sans", Arial, sans-serif;
    color: var(--ink);
  }
  .abs { position: absolute; }
  .center { text-align: center; left: 0; width: 1200px; }
  .script { font-family: "Dancing Script", cursive; font-weight: 700; color: var(--pink); }
  .btn {
    position: absolute; display: flex; align-items: center; justify-content: center;
    color: var(--white); font-weight: 600; font-size: 15px; border-radius: 2px;
  }
  .btn--pink { background: var(--pink); }
  .btn--teal { background: var(--teal); }

  /* Header */
  .site-header { top: 0; left: 0; width: 1200px; height: 72px; background: var(--white); }
  .brand { left: 196px; top: 20px; font-size: 28px; font-weight: 700; color: var(--teal-dark); }
  .nav a { position: absolute; top: 28px; font-size: 13px; font-weight: 600; color: var(--blue); text-decoration: none; }

  /* Hero */
  .hero { top: 72px; left: 0; width: 1200px; height: 511px;
    background: linear-gradient(180deg, #5d8fb4 0%, #7aa6c6 62%, #e2b27a 64%, #d99d5e 100%); }
  .hero-products { left: 145px; top: 140px; width: 830px; height: 371px; border-radius: 6px;
    background: radial-gradient(ellipse at 50% 55%, #e9d8c3 0%, #c79a6c 45%, rgba(199,154,108,0) 75%); }
  .hero-title { top: 112px; font-family: "Dancing Script", cursive; font-weight: 700; font-size: 34px; color: var(--white); }

  /* Supplies */
  .supplies { top: 598px; left: 0; width: 1200px; height: 315px; background: var(--paper); }
  .section-title { font-size: 46px; }
  .lead { font-size: 13px; color: var(--ink); }
  .supplies-strip { left: 272px; top: 825px; width: 641px; height: 88px;
    background: linear-gradient(90deg, #e7c3d6, #f2a0c3 20%, #a8d2ee 45%, #f4e06a 65%, #9ad6a4 82%, #d9dce6); border-radius: 40px 40px 0 0; }

  .rule { height: 1px; background: var(--line); }

  /* How it works */
  .step { position: absolute; top: 1018px; width: 270px; text-align: center; }
  .step-icon { display: block; margin: 0 auto; }
  .step h3 { margin-top: 22px; font-size: 15px; font-weight: 600; }
  .step p { margin-top: 16px; font-size: 12.5px; line-height: 18px; color: var(--muted); }

  /* What's inside */
  .inside { top: 1238px; left: 0; width: 1200px; height: 487px; background: var(--cream); }
  .inside-title { left: 177px; top: 1300px; }
  .inside-lead { left: 177px; top: 1362px; width: 430px; font-size: 13px; line-height: 22px; }
  .feature { position: absolute; right: 691px; text-align: right; }
  .feature h4 { font-size: 14px; font-weight: 600; color: var(--blue); }
  .feature p { font-size: 10px; color: var(--muted); margin-top: 3px; }
  .inside-box { left: 612px; top: 1305px; width: 413px; height: 342px;
    background: linear-gradient(160deg, #7fd9c9 0%, #9c6fc2 22%, #4e4b5a 55%, #d8a64c 80%, #5fb98f 100%); }

  /* Plans */
  .plans { top: 1725px; left: 0; width: 1200px; height: 621px; background: var(--mint); }
  .plans-bg { top: 1725px; left: 0; width: 1200px; height: 621px;
    background: radial-gradient(ellipse at 20% 30%, rgba(255,255,255,.7), rgba(255,255,255,0) 50%),
                radial-gradient(ellipse at 85% 40%, rgba(190,215,222,.8), rgba(190,215,222,0) 55%); }
  .plan { position: absolute; background: var(--white); border: 3px solid var(--pink); border-radius: 4px; text-align: center; }
  .plan--featured { border-color: var(--blue); }
  .plan h3 { font-size: 24px; font-weight: 700; margin-top: 16px; }
  .plan .price { font-size: 14px; margin-top: 2px; }
  .plan .ship { font-size: 10px; color: var(--muted); }
  .plan-photo { position: absolute; left: 36px; width: 196px; border-radius: 3px; }
  .plan .btn { left: 72px; width: 122px; height: 32px; }
  .badge { left: 682px; top: 1890px; width: 62px; height: 62px; border-radius: 50%; background: var(--blue);
    color: var(--white); font-size: 9px; font-weight: 700; line-height: 11px; display: flex; align-items: center; justify-content: center; text-align: center; }
  .guarantee { top: 2282px; font-size: 16px; }

  /* Testimonials */
  .quote-mark { top: 2490px; font-size: 72px; font-weight: 700; color: var(--pink); line-height: 1; font-family: Georgia, serif; }
  .quote { left: 260px; top: 2554px; width: 680px; text-align: center; font-size: 12.5px; font-style: italic; line-height: 20px; color: var(--muted); }
  .quote cite { color: var(--teal-dark); font-style: italic; }
  .arrow { top: 2573px; }

  /* Footer */
  .foot-col { position: absolute; top: 2703px; }
  .foot-col h5 { font-size: 14px; font-weight: 600; color: var(--pink); }
  .foot-col ul { list-style: none; margin-top: 14px; }
  .foot-col li { font-size: 12.5px; color: var(--muted); height: 22.5px; }
  .foot-col li::before { content: "›"; color: var(--teal-dark); margin-right: 10px; font-weight: 700; }
  .foot-col p { font-size: 12.5px; line-height: 20px; color: var(--muted); margin-top: 14px; width: 200px; }
  .email { position: absolute; left: 618px; top: 2788px; width: 190px; height: 22px; border: 1px solid var(--line); font-size: 10px; font-style: italic; color: #999; padding: 4px 8px; }
  .email-send { position: absolute; left: 786px; top: 2788px; width: 22px; height: 22px; background: var(--teal); }
  .card { position: absolute; top: 2760px; width: 30px; height: 18px; border-radius: 2px; }
  .copyright { left: 177px; top: 2880px; font-size: 11px; color: var(--muted); }
  .social { position: absolute; top: 2870px; width: 30px; height: 30px; border-radius: 50%; border: 1px solid var(--line); }
</style>
</head>
<body>

<header class="abs site-header">
  <div class="abs brand">Quillnest</div>
  <nav class="nav">
    <a style="left:755px">Home</a>
    <a style="left:821px">About Us</a>
    <a style="left:905px">Get Started</a>
    <a style="left:999px">Login</a>
  </nav>
</header>

<section class="abs hero" role="img" aria-label="Photo of a wooden desk in front of a blue wall"></section>
<div class="abs hero-products" role="img" aria-label="Photo of an opened supply box with craft kits, pencils, glue and stickers"></div>
<h1 class="abs center hero-title">Amazing school supplies delivered to your door every month</h1>
<div class="btn btn--pink" style="left:466px;top:170px;width:126px;height:38px">Get started</div>
<div class="btn btn--teal" style="left:608px;top:170px;width:124px;height:38px">Give a gift</div>

<section class="abs supplies"></section>
<h2 class="abs center script section-title" style="top:632px">Our School Supplies</h2>
<p class="abs center lead" style="top:697px">Excepteur sint occaecat cupidatat non proident, sunt in culpa qui officia</p>
<div class="btn btn--teal" style="left:526px;top:752px;width:162px;height:38px">View all items</div>
<div class="abs supplies-strip" role="img" aria-label="Photo of colourful scissors, pencils, rulers and highlighters"></div>

<div class="abs rule" style="left:190px;top:913px;width:820px"></div>

<h2 class="abs center script section-title" style="top:941px">How it works</h2>
<div class="step" style="left:172px">
  <svg class="step-icon" width="80" height="80" viewBox="0 0 80 80">
    <circle cx="40" cy="40" r="40" fill="#bfe6f7"/><circle cx="40" cy="40" r="34" fill="var(--blue)"/>
    <path d="M31 38h18l-3 18H34z" fill="#fff"/>
    <path d="M36 38l-3-14M40 38v-16M44 38l4-13" stroke="#fff" stroke-width="2.5" stroke-linecap="round"/>
  </svg>
  <h3>Box of Happiness</h3>
  <p>Lorem ipsum dolor sit amet, consectetuer adipis cing elit, sed diam nonummy nibh eulaoreet dolore</p>
</div>
<div class="step" style="left:465px">
  <svg class="step-icon" width="80" height="80" viewBox="0 0 80 80">
    <circle cx="40" cy="40" r="40" fill="#bfe6f7"/><circle cx="40" cy="40" r="34" fill="var(--blue)"/>
    <path d="M28 58V36a12 12 0 0 1 24 0v22z" fill="#fff"/>
    <path d="M40 26v32M28 44h24" stroke="var(--blue)" stroke-width="2.5"/>
  </svg>
  <h3>Get at your Doorstep</h3>
  <p>Lorem ipsum dolor sit amet, consectetuer adipis cing elit, sed diam nonummy nibh eulaoreet dolore</p>
</div>
<div class="step" style="left:756px">
  <svg class="step-icon" width="80" height="80" viewBox="0 0 80 80">
    <circle cx="40" cy="40" r="40" fill="#bfe6f7"/><circle cx="40" cy="40" r="34" fill="var(--blue)"/>
    <circle cx="40" cy="40" r="16" fill="none" stroke="#fff" stroke-width="3"/>
  </svg>
  <h3>Enjoy School days</h3>
  <p>Lorem ipsum dolor sit amet, consectetuer adipis cing elit, sed diam nonummy nibh eulaoreet dolore</p>
</div>

<div class="abs rule" style="left:190px;top:1237px;width:820px"></div>

<section class="abs inside"></section>
<h2 class="abs script section-title inside-title">What's inside?</h2>
<p class="abs inside-lead">Lorem ipsum dolor sit amet, consectetur adipiscing elit, sed do eius mod tempor incididunt ut labore et dolore magna aliqua.</p>
<div class="feature" style="top:1434px"><h4>Note books</h4><p>(Lipsum dolor sit amet, ullamcorper suscipit lobortis nisl ut aliquip)</p></div>
<div class="feature" style="top:1484px"><h4>Pencil box accessories</h4><p>(Et illum dolore eu feugiat nulla facilisis at vero eros et accumsan)</p></div>
<div class="feature" style="top:1539px"><h4>Craft kits</h4><p>(Nam liber tempor cum soluta nobis eleifend)</p></div>
<div class="feature" style="top:1593px"><h4>Stickers</h4><p>(Claritas est etiam processus dynamicus, qui sequitur mutationem)</p></div>
<svg class="abs" style="left:509px;top:1430px" width="200" height="190" viewBox="0 0 200 190">
  <g stroke="var(--teal-dark)" stroke-width="1.5" fill="var(--teal-dark)">
    <line x1="4" y1="14" x2="165" y2="14"/><circle cx="165" cy="14" r="2.5"/>
    <line x1="4" y1="64" x2="155" y2="64"/><circle cx="155" cy="64" r="2.5"/>
    <line x1="4" y1="119" x2="140" y2="119"/><circle cx="140" cy="119" r="2.5"/>
    <line x1="4" y1="173" x2="150" y2="173"/><circle cx="150" cy="173" r="2.5"/>
  </g>
</svg>
<div class="abs inside-box" role="img" aria-label="Photo of an open teal and purple box filled with notebooks, pens, craft kits and stickers"></div>

<section class="abs plans"></section>
<div class="abs plans-bg" role="img" aria-label="Soft blurred photo of a bright classroom desk"></div>
<h2 class="abs center script section-title" style="top:1759px">Choose a plan</h2>
<p class="abs lead" style="left:290px;top:1828px;width:620px;text-align:center;line-height:21px">Lorem ipsum dolor sit amet, consectetur adipiscing elit, sed do eius mod tempor incididunt ut labore et dolore magna aliqua.</p>

<div class="plan" style="left:173px;top:1965px;width:268px;height:272px">
  <h3>Monthly Plan</h3>
  <p class="price">$00.00/ Month</p>
  <p class="ship">(plus shipping)</p>
  <div class="plan-photo" style="top:92px;height:124px;background:linear-gradient(135deg,#d9b98a,#c99e6b 45%,#f06fa0 70%,#6ac6e8)" role="img" aria-label="Photo of a single supply box with notebooks and pencils"></div>
  <div class="btn btn--pink" style="top:224px">Get Started</div>
</div>
<div class="plan plan--featured" style="left:466px;top:1919px;width:268px;height:318px">
  <h3>6 Month Plan</h3>
  <p class="price">$00.00/ Month</p>
  <p class="ship">(plus shipping)</p>
  <div class="plan-photo" style="top:98px;height:164px;background:linear-gradient(160deg,#6fd6c7,#4fc4b5 50%,#f3a64d 75%,#e3588f)" role="img" aria-label="Photo of a stack of six teal supply boxes with school supplies"></div>
  <div class="btn btn--pink" style="top:270px">Get Started</div>
</div>
<div class="plan" style="left:757px;top:1965px;width:268px;height:272px">
  <h3>12 Month Plan</h3>
  <p class="price">$00.00/ Month</p>
  <p class="ship">(plus shipping)</p>
  <div class="plan-photo" style="top:92px;height:124px;background:linear-gradient(160deg,#6fd6c7,#55c7b8 45%,#e5c27a 70%,#d9534f)" role="img" aria-label="Photo of twelve teal supply boxes with books and pencils"></div>
  <div class="btn btn--pink" style="top:224px">Get Started</div>
</div>
<div class="abs badge">MOST<br>POPULAR</div>
<p class="abs center guarantee">Satisfaction guaranteed or your money back. Plans automatically renew. You may cancel at any time.</p>

<h2 class="abs center script section-title" style="top:2384px">Happy Emotions</h2>
<p class="abs center lead" style="top:2462px">Excepteur sint occaecat cupidatat non proident, sunt in culpa qui officia</p>
<div class="abs center quote-mark">”</div>
<p class="abs quote">Sed ut perspiciatis unde omnis iste natus error sit voluptatem accusantium doloremque lauda ntium, totam rem aperiam, eaque ipsa quae ab illo inventore veritatis et quasi architecto beatae vitae dicta sunt explicabo. Nemo enim ipsam voluptatem quia voluptas sit aspernatur aut odit aut eos qui. &nbsp;<cite>- Marisol</cite></p>
<svg class="abs arrow" style="left:188px" width="12" height="16" viewBox="0 0 12 16"><path d="M9 2L3 8l6 6" fill="none" stroke="#333" stroke-width="2"/></svg>
<svg class="abs arrow" style="left:996px" width="12" height="16" viewBox="0 0 12 16"><path d="M3 2l6 6-6 6" fill="none" stroke="#333" stroke-width="2"/></svg>

<div class="abs rule" style="left:173px;top:2655px;width:854px"></div>

<footer>
  <div class="foot-col" style="left:177px">
    <h5>About Quillnest</h5>
    <ul><li>About us</li><li>Our supplies</li><li>How it works</li><li>Blog</li></ul>
  </div>
  <div class="foot-col" style="left:398px">
    <h5>Support</h5>
    <ul><li>Contact us</li><li>Shipping rates</li><li>Delivery times</li><li>FAQs</li><li>Gift card</li></ul>
  </div>
  <div class="foot-col" style="left:618px">
    <h5>Newsletter</h5>
    <p>Subscribe to our newsletter and know about our latest offers.</p>
  </div>
  <div class="email">Enter email id...</div>
  <svg class="email-send" viewBox="0 0 22 22"><path d="M6 11l10-5-3 11-2-4z" fill="#fff"/></svg>
  <div class="foot-col" style="left:839px">
    <h5>Payment option</h5>
  </div>
  <div class="abs" style="left:845px;top:2742px;width:142px;height:44px;border:1px solid var(--line)"></div>
  <div class="card" style="left:851px;background:#1a3f8f"></div>
  <div class="card" style="left:884px;background:#e9762b"></div>
  <div class="card" style="left:917px;background:#2a8fd6"></div>
  <div class="card" style="left:950px;background:#cccccc"></div>

  <div class="abs rule" style="left:173px;top:2865px;width:854px"></div>
  <p class="abs copyright">Copyright © Quillnest 2017</p>
  <div class="social" style="left:911px"></div>
  <div class="social" style="left:951px"></div>
  <div class="social" style="left:991px"></div>
</footer>

</body>
</html>
```